Quilvo Garage Doors Business Card

I need a Business Card for my garage door business:
Quilvo Garage Doors.
please add:
logo
phone number: 855-3-QUILVO
(853-392)

email: service@quilvogaragedoors.com
website: www.quilvogaragedoors.com

The attached image is recommendation ONLY.

```html
<!DOCTYPE html>
<html lang="en">
<head>
<meta charset="utf-8">
<title>Quilvo Garage Doors – Business Card</title>
<link href="https://fonts.googleapis.com/css2?family=Open+Sans:wght@400;600;700&display=swap" rel="stylesheet">
<style>
  :root {
    --ink: #1f1d1e;
    --teal: #47b3bf;
    --white: #f2f2f2;
    --muted: #d9d9d9;
    --backdrop: #e9e6e1;
  }
  * { margin: 0; padding: 0; box-sizing: border-box; }
  html, body { width: 1200px; height: 899px; overflow: hidden; }
  body {
    background: var(--backdrop);
    font-family: "Open Sans", Arial, sans-serif;
    position: relative;
  }
  .card {
    position: absolute;
    top: 306px;
    width: 500px;
    height: 286px;
    background: var(--ink);
    border-radius: 4px;
    overflow: hidden;
    box-shadow: 0 14px 30px rgba(0,0,0,.22);
  }
  .card--back { left: 70px; }
  .card--front { left: 630px; }
  .card__shapes { position: absolute; inset: 0; }

  .brand {
    position: absolute;
    color: var(--white);
    font-weight: 600;
    line-height: 1.1;
    display: flex;
    align-items: center;
    gap: 12px;
  }
  .brand__mark {
    width: 30px; height: 30px;
    background: var(--teal);
    border-radius: 5px;
    flex: none;
  }
  .card--back .brand { left: 235px; top: 112px; font-size: 26px; }
  .card--front .brand { left: 28px; top: 36px; font-size: 19px; }

  .person { position: absolute; left: 48px; top: 120px; }
  .person__name { color: var(--teal); font-weight: 700; font-size: 20px; line-height: 1.1; }
  .person__title { color: var(--muted); font-size: 12px; }
  .person__tab {
    position: absolute; left: 28px; top: 124px;
    width: 12px; height: 36px; background: var(--teal);
  }

  .contacts { position: absolute; left: 28px; top: 180px; list-style: none; }
  .contacts li {
    display: flex; align-items: center; gap: 10px;
    color: var(--white); font-size: 13.5px; line-height: 26px;
  }
  .contacts svg { width: 16px; height: 16px; flex: none; }
</style>
</head>
<body>

  <section class="card card--back" aria-label="Card back">
    <svg class="card__shapes" viewBox="0 0 500 286" aria-hidden="true">
      <path d="M0 22 H178 Q198 22 198 42 V120 L100 286 H0 Z" fill="var(--teal)"/>
    </svg>
    <div class="brand">Quilvo Garage Doors</div>
  </section>

  <section class="card card--front" aria-label="Card front">
    <svg class="card__shapes" viewBox="0 0 500 286" aria-hidden="true">
      <path d="M338 0 H500 V34 L430 112 H360 Q344 112 338 98 L310 22 Q304 0 338 0 Z" fill="var(--teal)"/>
      <line x1="28" y1="98" x2="300" y2="98" stroke="var(--teal)" stroke-width="1"/>
      <path d="M0 274 L500 262 V276 L0 286 Z" fill="var(--teal)"/>
    </svg>

    <div class="brand"><span class="brand__mark"></span>Quilvo Garage Doors</div>

    <span class="person__tab"></span>
    <div class="person">
      <div class="person__name">Your Name</div>
      <div class="person__title">Job Title</div>
    </div>

    <ul class="contacts">
      <li>
        <svg viewBox="0 0 16 16" aria-hidden="true"><circle cx="8" cy="8" r="8" fill="var(--teal)"/><path d="M5 4.5 L6.8 4.5 L7.4 6.5 L6.4 7.3 Q7.3 9 8.8 9.7 L9.6 8.7 L11.5 9.3 L11.5 11 Q7.5 11.5 5 7 Z" fill="var(--ink)"/></svg>
        855 - 3 - QUILVO (853-392)
      </li>
      <li>
        <svg viewBox="0 0 16 16" aria-hidden="true"><circle cx="8" cy="8" r="8" fill="var(--teal)"/><rect x="4" y="5" width="8" height="6" fill="var(--ink)"/><path d="M4 5 L8 8.5 L12 5" stroke="var(--teal)" fill="none" stroke-width="1"/></svg>
        service@quilvogaragedoors.com
      </li>
      <li>
        <svg viewBox="0 0 16 16" aria-hidden="true"><circle cx="8" cy="8" r="8" fill="var(--teal)"/><circle cx="8" cy="8" r="4.5" fill="none" stroke="var(--ink)" stroke-width="1.2"/><path d="M3.5 8 H12.5 M8 3.5 Q5.5 8 8 12.5 Q10.5 8 8 3.5" fill="none" stroke="var(--ink)" stroke-width="1"/></svg>
        www.quilvogaragedoors.com
      </li>
    </ul>
  </section>

</body>
</html>
```